Varlow Landscaping

Create a website for a new landscaping company. I have a logo already and description of services offered. I have a website that I would like all inquiries and appointments to get forwarded to. I need just need it well organized so that a husband and wife team can manage it easily. This is a company that will continue to grow over time and will need to add more services under new tabs over time. If you need the email where appointments and inquiries should go please send me a message.
Services offered are: Weekly/bi weekly mowing, weed eating and edging, Plant installation pinestraw & mulch installation, weed & feed, leaf removal and yard clean up.

```html
<!DOCTYPE html>
<html lang="en">
<head>
<meta charset="utf-8">
<title>Varlow Lawn Care &amp; Landscaping</title>
<link href="https://fonts.googleapis.com/css2?family=Montserrat:wght@400;600;700&family=Roboto:wght@400;500;700&display=swap" rel="stylesheet">
<style>
:root{
  --green:#1d5a1c;
  --green-dark:#174a16;
  --gold:#d4a90f;
  --ink:#1d1d1d;
  --muted:#555;
  --footer:#1c2216;
  --white:#fff;
  --line:#cfcfcf;
}
*{box-sizing:border-box;margin:0;padding:0}
html,body{width:1200px;height:3891px;overflow:hidden}
body{position:relative;font-family:'Roboto',sans-serif;color:var(--ink);background:var(--white)}
.abs{position:absolute}
.head{font-family:'Montserrat',sans-serif}
.btn{position:absolute;display:flex;align-items:center;justify-content:center;font-family:'Roboto',sans-serif;font-weight:700;font-size:14px;border-radius:4px}
.btn-green{background:var(--green);color:var(--white)}
.rule{position:absolute;height:4px;background:var(--gold)}
.photo{position:absolute}

/* header */
.topbar{left:0;top:0;width:1200px;height:6px;background:var(--gold)}
.header{left:0;top:6px;width:1200px;height:66px;background:var(--white);z-index:3}
.brand{left:112px;top:6px;width:213px;height:206px;z-index:4}
.brand-name{position:absolute;left:0;top:68px;width:213px;text-align:center;font-family:'Montserrat',sans-serif;font-weight:700;color:var(--green);font-size:26px;line-height:1.1}
.brand-name small{display:block;font-size:12px;margin-top:4px}
.nav a{position:absolute;top:34px;font-size:15px;color:var(--ink);text-decoration:none;z-index:4}
.nav a.active{color:var(--green);font-weight:500}
.nav .bar{position:absolute;left:405px;top:68px;width:40px;height:4px;background:var(--green);z-index:4}

/* hero */
.hero{left:0;top:72px;width:1200px;height:729px;background:linear-gradient(180deg,#3e6a2a 0%,#4f7d2f 45%,#6c7a2c 70%,#5b3a26 100%)}
.hero h1{position:absolute;left:103px;top:282px;font-family:'Montserrat',sans-serif;font-weight:700;font-size:61px;line-height:71px;color:var(--white)}
.hero p{position:absolute;left:112px;top:512px;font-family:'Montserrat',sans-serif;font-weight:600;font-size:18px;color:var(--white)}

/* section title */
.title{position:absolute;font-family:'Montserrat',sans-serif;font-size:45px;font-weight:400;white-space:nowrap}
.title b{font-weight:700;color:var(--green)}

/* tabs */
.tab{position:absolute;top:936px;font-size:16px;transform:translateX(-50%);white-space:nowrap}
.tab.active{color:var(--green);font-weight:500}
.card{position:absolute;top:1029px;width:315px;height:351px;background:var(--white);box-shadow:0 3px 8px rgba(0,0,0,.22);border-radius:4px;overflow:hidden}
.card .label{position:absolute;left:0;top:292px;width:100%;text-align:center;font-size:20px}
.card.active .label{color:var(--green);font-weight:500}

/* why */
.why-list{position:absolute;left:642px;top:1611px}
.why-item{position:relative;height:73px;display:flex;align-items:center}
.why-item .ic{width:60px;height:60px;border-radius:50%;background:var(--white);display:flex;align-items:center;justify-content:center}
.why-item .ic.gold{background:var(--gold)}
.why-item span{margin-left:17px;font-family:'Montserrat',sans-serif;font-size:18px;color:var(--white);font-weight:500}

/* about */
.about-text{position:absolute;left:115px;width:449px;font-size:13px;line-height:30px;color:var(--muted);text-align:justify}

/* newsletter */
.field{position:absolute;top:3296px;height:40px;border:1px solid #bdbdbd;border-radius:3px;font-size:13px;color:#777;padding:12px 14px}

/* footer */
.footer-h{position:absolute;font-size:16px;font-weight:500;color:var(--gold)}
.flink{position:absolute;left:115px;font-size:13px;color:var(--white)}
.contact{position:absolute;left:896px;display:flex;align-items:center;font-size:13px;color:var(--white)}
.contact svg{margin-right:12px}
</style>
</head>
<body>

<div class="abs topbar"></div>
<div class="abs header"></div>

<div class="abs brand">
  <svg width="213" height="206" viewBox="0 0 213 206"><path d="M0 0H213V160L106 206L0 160Z" fill="#fff"/></svg>
  <div class="brand-name">VARLOW<small>LAWN CARE &amp; LANDSCAPING</small></div>
</div>

<nav class="nav">
  <a class="active" style="left:405px">Home</a>
  <a style="left:476px">About Us</a>
  <a style="left:568px">Services</a>
  <a style="left:659px">Why Choose Us</a>
  <a style="left:798px">Contact Us</a>
  <span class="bar"></span>
</nav>
<div class="btn btn-green" style="left:910px;top:23px;width:178px;height:39px;z-index:4">Book an Appointment</div>

<section class="abs hero">
  <div class="photo" role="img" aria-label="Landscaper mowing a green lawn beside flowering shrubs" style="inset:0;background:linear-gradient(120deg,rgba(30,60,20,.5),rgba(80,140,50,.15) 55%,rgba(150,40,40,.25))"></div>
  <h1 style="top:210px">Professional Lawn<br>&amp; Landscape Care<br>You Can Trust</h1>
  <p style="top:440px">Residential lawn maintenance, cleanups, and seasonal services</p>
  <div class="btn btn-green" style="left:110px;top:484px;width:111px;height:41px">Get a Quote</div>
  <svg class="abs" style="left:0;top:620px" width="1200" height="110" viewBox="0 0 1200 110">
    <path d="M0 110 Q600 -20 1200 110Z" fill="#d4a90f"/>
    <path d="M0 110 Q600 20 1200 110Z" fill="#fff"/>
  </svg>
</section>

<h2 class="title" style="left:461px;top:822px">What <b>We Do</b></h2>
<div class="rule" style="left:562px;top:882px;width:82px"></div>

<div class="tab" style="left:311px">Lawn Maintenance</div>
<div class="tab active" style="left:514px">Landscape Installation</div>
<div class="tab" style="left:710px">Lawn Treatments</div>
<div class="tab" style="left:892px">Seasonal Services</div>
<div class="abs" style="left:245px;top:970px;width:710px;height:3px;background:var(--line)"></div>
<div class="abs" style="left:432px;top:969px;width:168px;height:4px;background:var(--green)"></div>

<div class="card" style="left:111px">
  <div class="photo" role="img" aria-label="Gloved hands planting flowers in gravel" style="left:0;top:0;width:315px;height:290px;background:linear-gradient(135deg,#5f665a,#8a917f)"></div>
  <svg class="abs" style="left:0;top:240px" width="315" height="52"><path d="M0 52 Q157 -30 315 52Z" fill="#fff"/></svg>
  <div class="label">Plant Installation</div>
</div>
<div class="card active" style="left:441px">
  <div class="photo" role="img" aria-label="Garden bed covered with pine straw under trees" style="left:0;top:0;width:315px;height:290px;background:linear-gradient(160deg,#9a8a5a,#5f7a3a 60%,#3f5a2a)"></div>
  <svg class="abs" style="left:0;top:240px" width="315" height="52"><path d="M0 52 Q157 -30 315 52Z" fill="#fff"/></svg>
  <svg class="abs" style="left:125px;top:216px" width="66" height="66"><circle cx="33" cy="33" r="32" fill="#fff"/><circle cx="33" cy="33" r="26" fill="#1d5a1c"/><circle cx="36" cy="30" r="8" fill="none" stroke="#fff" stroke-width="3"/><path d="M30 36 L22 44" stroke="#fff" stroke-width="3" stroke-linecap="round"/></svg>
  <div class="label">Pine Straw Installation</div>
</div>
<div class="card" style="left:771px">
  <div class="photo" role="img" aria-label="Worker spreading dark mulch beneath a shrub" style="left:0;top:0;width:315px;height:290px;background:linear-gradient(160deg,#4f7a35,#2f4a22 60%,#2a1e16)"></div>
  <svg class="abs" style="left:0;top:240px" width="315" height="52"><path d="M0 52 Q157 -30 315 52Z" fill="#fff"/></svg>
  <div class="label">Mulch Installation</div>
</div>

<section class="abs" style="left:0;top:1470px;width:1200px;height:546px;background:linear-gradient(135deg,#2f6e26,#1c4f19)">
  <div class="photo" role="img" aria-label="Crew planting trees and tulips in a park lawn" style="left:0;top:0;width:610px;height:546px;background:linear-gradient(180deg,#6f8f4a,#4f8a2f 50%,#7a3a2a 85%,#caa04a)"></div>
  <svg class="abs" style="left:540px;top:0" width="80" height="546" viewBox="0 0 80 546"><path d="M32 0 Q110 273 32 546 H80 V0Z" fill="#fff"/><path d="M38 0 Q118 273 38 546 H80 V0Z" fill="#256522"/></svg>
</section>
<h2 class="title" style="left:636px;top:1514px;color:#fff">Why <b style="color:#fff">Choose Us</b></h2>
<div class="rule" style="left:644px;top:1577px;width:81px"></div>
<div class="why-list">
  <div class="why-item"><div class="ic"><svg width="28" height="24"><path d="M14 2 L26 12 H22 V22 H6 V12 H2Z" fill="#1d5a1c"/></svg></div><span>Family-Owned &amp; Operated</span></div>
  <div class="why-item"><div class="ic"><svg width="26" height="28"><path d="M13 2 L24 6 V14 Q24 22 13 26 Q2 22 2 14 V6Z" fill="#1d5a1c"/><path d="M8 14 L12 18 L18 10" stroke="#fff" stroke-width="2.5" fill="none"/></svg></div><span>Reliable Scheduling</span></div>
  <div class="why-item"><div class="ic gold"><svg width="26" height="26"><path d="M4 14 L14 4 H22 V12 L12 22Z" fill="#fff"/><circle cx="18" cy="8" r="2" fill="#d4a90f"/></svg></div><span>Affordable Pricing</span></div>
  <div class="why-item"><div class="ic"><svg width="12" height="30"><circle cx="6" cy="4" r="4" fill="#1d5a1c"/><rect x="2" y="11" width="8" height="18" fill="#1d5a1c"/></svg></div><span>Attention to Detail</span></div>
  <div class="why-item"><div class="ic"><svg width="30" height="24"><path d="M2 20 L11 11 L16 16 L26 6" stroke="#1d5a1c" stroke-width="4" fill="none"/><path d="M20 4 H28 V12Z" fill="#1d5a1c"/></svg></div><span>Growing Local Business</span></div>
</div>

<h2 class="title" style="left:112px;top:2097px">About <b>Us</b></h2>
<div class="rule" style="left:112px;top:2165px;width:82px"></div>
<p class="about-text" style="top:2194px">Varlow Landscaping is a family-owned and operated lawn care and landscaping company built on reliability, honest work, and attention to detail. As a husband-and-wife team, we take pride in providing personalized service and treating every property as if it were our own.</p>
<p class="about-text" style="top:2332px;line-height:27px">We started Varlow Landscaping with a simple mission — to deliver dependable, high-quality outdoor services that homeowners can trust season after season.</p>
<div class="btn btn-green" style="left:112px;top:2439px;width:110px;height:39px">Read More</div>
<div class="photo" role="img" aria-label="Aerial view of a mower on a lawn beside a curved garden path" style="left:780px;top:2111px;width:308px;height:384px;border-radius:4px;background:linear-gradient(150deg,#3f6a2a,#5f9a3a 55%,#b8a888 70%,#4f8a2f)"></div>
<div class="photo" role="img" aria-label="Rake gathering autumn leaves" style="left:620px;top:2287px;width:248px;height:212px;border:4px solid #fff;border-radius:8px;background:linear-gradient(135deg,#b8451a,#e07a2a 50%,#8a3a18)"></div>

<section class="abs" style="left:0;top:2599px;width:1200px;height:444px">
  <div class="photo" role="img" aria-label="Front porch of a house with colorful shrubs and green lawn" style="inset:0;background:linear-gradient(180deg,#6a6470 0%,#7a6a5a 30%,#c0a83a 45%,#3f7a2a 65%,#2f6a22 100%)"></div>
  <div class="head abs" style="left:119px;top:290px;font-size:45px;line-height:57px;color:#fff">Ready To Transform<br><b>Your Lawn?</b></div>
  <div class="btn" style="left:710px;top:327px;width:178px;height:39px;background:#fff;color:var(--ink)">Book an Appointment</div>
  <div class="btn" style="left:907px;top:327px;width:179px;height:39px;background:var(--gold);color:#fff">Request a Free Quote</div>
</section>

<h2 class="title" style="left:378px;top:3122px">Join <b>Our Newsletter</b></h2>
<div class="rule" style="left:558px;top:3186px;width:84px"></div>
<p class="abs" style="left:0;top:3220px;width:1200px;text-align:center;font-size:13px;line-height:27px;color:var(--muted)">Subscribe to receive helpful lawn care tips, seasonal service reminders, and special promotions from<br>Varlow Landscaping — delivered straight to your inbox.</p>
<div class="field" style="left:110px;width:357px">Name</div>
<div class="field" style="left:479px;width:431px">Email</div>
<div class="btn btn-green" style="left:917px;top:3296px;width:173px;height:40px">Subscribe Now</div>

<footer class="abs" style="left:0;top:3395px;width:1200px;height:496px;background:var(--footer)">
  <svg class="abs" style="left:0;top:0" width="1200" height="100" viewBox="0 0 1200 100">
    <path d="M0 0 H1200 V4 Q600 190 0 4Z" fill="#fff"/>
    <path d="M40 14 Q600 140 1160 14 Q600 100 40 14Z" fill="#d4a90f"/>
  </svg>
  <div class="footer-h" style="left:115px;top:191px">QUICK LINKS</div>
  <div class="flink" style="top:226px">Home</div>
  <div class="flink" style="top:259px">About Us</div>
  <div class="flink" style="top:293px">Services</div>
  <div class="flink" style="top:326px">Why Choose Us</div>
  <div class="flink" style="top:360px">Contact Us</div>

  <div class="head abs" style="left:400px;top:258px;width:400px;text-align:center;font-weight:700;font-size:34px;line-height:1;color:var(--green)">VARLOW<div style="font-size:15px;margin-top:8px">LAWN CARE &amp; LANDSCAPING</div></div>
  <svg class="abs" style="left:538px;top:396px" width="140" height="30">
    <circle cx="15" cy="15" r="13" fill="#2f7a2a"/><circle cx="51" cy="15" r="13" fill="#fff"/><circle cx="88" cy="15" r="13" fill="#fff"/><circle cx="124" cy="15" r="13" fill="#fff"/>
  </svg>

  <div class="footer-h" style="left:882px;top:188px">CONTACT INFO</div>
  <div class="contact" style="top:228px"><svg width="20" height="20"><path d="M10 1 A7 7 0 0 1 17 8 C17 13 10 19 10 19 C10 19 3 13 3 8 A7 7 0 0 1 10 1Z" fill="#fff"/><circle cx="10" cy="8" r="2.6" fill="#1c2216"/></svg>Lorem Ipsum,USA -437916</div>
  <div class="contact" style="top:282px"><svg width="20" height="20"><circle cx="10" cy="10" r="9" fill="#fff"/><path d="M6 5 L8 5 L9 8 L8 9 Q9 11 11 12 L12 11 L15 12 L15 14 Q10 15 6 9Z" fill="#1c2216"/></svg>+1 888 888 8888</div>
  <div class="contact" style="top:337px"><svg width="20" height="20"><circle cx="10" cy="10" r="9" fill="#fff"/><rect x="5" y="6.5" width="10" height="7" fill="none" stroke="#1c2216" stroke-width="1.4"/><path d="M5 7 L10 11 L15 7" stroke="#1c2216" stroke-width="1.4" fill="none"/></svg>info@varlow.com</div>

  <div class="abs" style="left:115px;top:451px;width:973px;height:1px;background:#6a6a5a"></div>
  <div class="abs" style="left:0;top:467px;width:1200px;text-align:center;font-size:13px;color:#fff">Copyright © 2026 &nbsp;Varlow Lawn Care &amp; Landscaping.All rights reserved.</div>
</footer>

</body>
</html>
```